Poloshirt Packaging

We need a very attractive packaging design for our poloshirts. We are wholesaler of the schoolwear market. See what we currently have. I dont want any specific sizing put on the packaging. One design for all poloshirts (2 sides).
our logo is attached aswell

Target Market(s)

Parents

Requirements
Must have
• Our logo
Should not have
• size or age

```html
<!DOCTYPE html>
<html lang="en">
<head>
<meta charset="utf-8">
<title>Brightwear Poloshirt Packaging</title>
<link rel="stylesheet" href="https://fonts.googleapis.com/css2?family=Carlito:wght@400;700&family=Arimo:wght@700&display=swap">
<style>
  :root {
    --navy: #1b2f5e;
    --red: #e3262d;
    --ink: #111111;
    --paper: #ffffff;
  }
  * { margin: 0; padding: 0; box-sizing: border-box; }
  html, body {
    width: 1200px;
    height: 2213px;
    overflow: hidden;
    background: var(--paper);
  }
  .pack {
    position: relative;
    width: 1200px;
    height: 2213px;
    background: var(--paper);
    font-family: "Carlito", "Calibri", sans-serif;
    color: var(--ink);
  }
  .brand-name {
    position: absolute;
    left: 0;
    top: 270px;
    width: 1200px;
    text-align: center;
    font-family: "Carlito", "Calibri", sans-serif;
    font-weight: 400;
    font-size: 250px;
    line-height: 1;
    letter-spacing: -2px;
    color: var(--navy);
  }
  .product-line {
    position: absolute;
    left: 700px;
    top: 748px;
    width: 300px;
    text-align: center;
    font-family: "Arimo", "Arial", sans-serif;
    font-weight: 700;
    font-size: 44px;
    letter-spacing: 1px;
    color: var(--red);
  }
  .features-frame {
    position: absolute;
    left: 0;
    top: 0;
  }
  .features {
    position: absolute;
    left: 0;
    top: 0;
    list-style: none;
    font-size: 42px;
  }
  .features li {
    position: absolute;
    white-space: nowrap;
    line-height: 1;
  }
  .features li::before {
    content: "";
    position: absolute;
    left: -30px;
    top: 13px;
    width: 18px;
    height: 18px;
    border-radius: 50%;
    background: var(--ink);
  }
  .safety {
    position: absolute;
    left: 303px;
    top: 1934px;
    width: 594px;
    height: 180px;
    border: 2px solid var(--ink);
    transform: rotate(180deg);
    text-align: center;
    font-family: "Arimo", "Arial", sans-serif;
    padding-top: 18px;
  }
  .safety-title {
    font-weight: 700;
    font-size: 28px;
    letter-spacing: 6px;
    margin-bottom: 14px;
  }
  .safety-note {
    font-family: "Carlito", "Calibri", sans-serif;
    font-size: 30px;
    line-height: 1.2;
  }
</style>
</head>
<body>
<main class="pack">
  <h1 class="brand-name">Brightwear</h1>
  <p class="product-line">POLOSHIRT</p>

  <svg class="features-frame" width="1200" height="1600" viewBox="0 0 1200 1600" aria-hidden="true">
    <rect x="63" y="1129" width="1078" height="418" rx="42" fill="none" stroke="var(--navy)" stroke-width="5"/>
    <rect x="82" y="1149" width="1040" height="379" rx="30" fill="none" stroke="var(--red)" stroke-width="7"/>
  </svg>

  <ul class="features">
    <li style="left:155px; top:1174px;">Sold in 22 Colours</li>
    <li style="left:212px; top:1248px;">Superior Weight Fabric (210gms)</li>
    <li style="left:263px; top:1319px;">Easy Care - Low Iron</li>
    <li style="left:318px; top:1391px;">Reactive Dyed for Superb Colour</li>
    <li style="left:372px; top:1462px;">Strengthened with twin needle stitching</li>
  </ul>

  <section class="safety">
    <p class="safety-title">Safety First</p>
    <p class="safety-note">To Avoid Danger of Suffocation keep this<br>Wrapper away from Babie and Children.</p>
  </section>
</main>
</body>
</html>
```